Under 16 Cricket Tour To Malaysia

I need a flyer to promote an under 16 cricket to Malaysia
The tour will run from April 25th 2108 to May the 7th

Target Market(s)

Boys aged 15-16

Industry/Entity Type

Tour

Font styles to use
Serif

Colors
0255a3
ec1f27

Requirements
Must have
• Dates of the tour
• T20 and Limited Overs games against teams from 5 other countries.
• Name of the tournament is Kestrel Bay International Under 16 Cricket Tournament
• Level 3 coaches with international experience
• Contact Marcus at marcus@pellowfield.com.au for more information.

```html
<!DOCTYPE html>
<html lang="en">
<head>
<meta charset="utf-8">
<title>Kestrel Bay International Under 16 Cricket Tournament</title>
<link rel="stylesheet" href="https://fonts.googleapis.com/css2?family=Alfa+Slab+One&family=Roboto+Slab:wght@500;800&display=swap">
<style>
  :root {
    --navy: #222a6c;
    --deep: #1a2157;
    --royal: #3553a6;
    --red: #ec1f27;
    --white: #ffffff;
    --gold: #f6c324;
    --sun: #f9d33a;
  }
  html, body {
    margin: 0;
    padding: 0;
    width: 1200px;
    height: 1039px;
    overflow: hidden;
    background: var(--white);
  }
  .flyer {
    position: relative;
    width: 1200px;
    height: 1039px;
    overflow: hidden;
    background: var(--navy);
  }
  .backdrop {
    position: absolute;
    inset: 0;
  }
  .tour-info {
    position: absolute;
    left: 247px;
    top: 332px;
    width: 580px;
    margin: 0;
    text-align: center;
    font-family: "Roboto Slab", Georgia, serif;
    color: var(--white);
  }
  .tour-info__name {
    margin: 0 0 14px;
    font-weight: 800;
    font-size: 31px;
    line-height: 1.2;
    color: var(--gold);
  }
  .tour-info__detail {
    margin: 0 0 10px;
    font-weight: 500;
    font-size: 21px;
    line-height: 1.3;
  }
  .tour-info__contact {
    margin: 4px 0 0;
    font-weight: 500;
    font-size: 19px;
    line-height: 1.3;
  }
  .tour-info__contact strong {
    font-weight: 800;
    color: var(--gold);
  }
  .banner {
    position: absolute;
    left: 212px;
    top: 668px;
    width: 800px;
    height: 156px;
    background: var(--red);
    transform: rotate(-5deg);
    transform-origin: center;
    display: flex;
    flex-direction: column;
    align-items: center;
    justify-content: center;
    gap: 12px;
    font-family: "Roboto Slab", Georgia, serif;
    font-weight: 800;
  }
  .banner__title {
    margin: 0;
    color: var(--white);
    font-size: 50px;
    letter-spacing: 1px;
    line-height: 1;
  }
  .banner__dates {
    margin: 0;
    color: var(--gold);
    font-size: 38px;
    line-height: 1;
  }
  .sport-name {
    position: absolute;
    left: 700px;
    top: 900px;
    margin: 0;
    font-family: "Alfa Slab One", Georgia, serif;
    font-weight: 400;
    font-size: 88px;
    line-height: 1;
    letter-spacing: 2px;
    color: var(--gold);
    -webkit-text-stroke: 4px var(--navy);
    paint-order: stroke fill;
  }
</style>
</head>
<body>
<main class="flyer">
  <svg class="backdrop" width="1200" height="1039" viewBox="0 0 1200 1039">
    <defs>
      <radialGradient id="circle-tone" cx="50%" cy="25%" r="75%">
        <stop offset="0" stop-color="var(--royal)"/>
        <stop offset="1" stop-color="var(--deep)"/>
      </radialGradient>
      <radialGradient id="sun-tone" cx="50%" cy="50%" r="50%">
        <stop offset="0" stop-color="var(--sun)"/>
        <stop offset="1" stop-color="var(--royal)"/>
      </radialGradient>
      <linearGradient id="player-tone" x1="0" y1="0" x2="1" y2="1">
        <stop offset="0" stop-color="var(--gold)"/>
        <stop offset="1" stop-color="var(--royal)"/>
      </linearGradient>
    </defs>

    <g class="stripes">
      <rect x="0" y="550" width="1034" height="489" fill="var(--white)"/>
      <rect x="0" y="550" width="1034" height="48" fill="var(--red)"/>
      <rect x="0" y="646" width="1034" height="48" fill="var(--red)"/>
      <rect x="0" y="742" width="1034" height="48" fill="var(--red)"/>
      <rect x="0" y="838" width="1034" height="48" fill="var(--red)"/>
      <rect x="0" y="934" width="1034" height="48" fill="var(--red)"/>
    </g>

    <g class="side-stripes">
      <rect x="1034" y="0" width="166" height="1039" fill="var(--white)"/>
      <rect x="1034" y="0" width="166" height="48" fill="var(--red)"/>
      <rect x="1034" y="96" width="166" height="48" fill="var(--red)"/>
      <rect x="1034" y="192" width="166" height="48" fill="var(--red)"/>
      <rect x="1034" y="288" width="166" height="48" fill="var(--red)"/>
      <rect x="1034" y="384" width="166" height="48" fill="var(--red)"/>
      <rect x="1034" y="480" width="166" height="48" fill="var(--red)"/>
      <rect x="1034" y="576" width="166" height="48" fill="var(--red)"/>
      <rect x="1034" y="672" width="166" height="48" fill="var(--red)"/>
      <rect x="1034" y="768" width="166" height="48" fill="var(--red)"/>
      <rect x="1034" y="864" width="166" height="48" fill="var(--red)"/>
      <rect x="1034" y="960" width="166" height="48" fill="var(--red)"/>
    </g>

    <rect class="side-badge" x="1070" y="120" width="95" height="110" rx="10" fill="var(--royal)"
          role="img" aria-label="Small badge with a cricket ball"/>
    <rect class="side-badge" x="1070" y="345" width="95" height="100" rx="10" fill="var(--royal)"
          role="img" aria-label="Small badge with a cricket helmet"/>

    <circle class="ring" cx="537" cy="510" r="410" fill="none" stroke="var(--royal)" stroke-width="70"/>
    <circle class="ring-field" cx="537" cy="510" r="375" fill="url(#circle-tone)"/>

    <circle class="illustration" cx="537" cy="240" r="90" fill="url(#sun-tone)"
            role="img" aria-label="Illustration of a cricket player in a helmet holding a bat in front of a rising sun"/>
    <circle class="illustration" cx="185" cy="275" r="78" fill="var(--red)"
            role="img" aria-label="Illustration of a red cricket ball"/>
    <rect class="illustration" x="95" y="520" width="120" height="150" rx="18" fill="var(--royal)"
          role="img" aria-label="Illustration of cricket pads, stumps and gloves"/>
    <rect class="illustration" x="850" y="420" width="110" height="130" rx="18" fill="var(--gold)"
          role="img" aria-label="Illustration of a tournament trophy"/>
    <rect class="illustration" x="760" y="70" width="250" height="210" rx="24" fill="url(#player-tone)"
          role="img" aria-label="Illustration of a batsman swinging a bat"/>

    <polygon class="ribbon-tail" points="250,790 120,820 170,860 140,925 265,895" fill="var(--gold)"/>
    <polygon class="ribbon-tail" points="960,650 1090,630 1050,690 1110,740 980,760" fill="var(--gold)"/>
  </svg>

  <section class="tour-info">
    <h2 class="tour-info__name">Kestrel Bay International<br>Under 16 Cricket Tournament</h2>
    <p class="tour-info__detail">T20 and Limited Overs games against teams from 5 other countries</p>
    <p class="tour-info__detail">Level 3 coaches with international experience</p>
    <p class="tour-info__contact">Contact Marcus at <strong>marcus@pellowfield.com.au</strong><br>for more information.</p>
  </section>

  <div class="banner">
    <h1 class="banner__title">UNDER 16 TOURNAMENT</h1>
    <p class="banner__dates">April 25th 2018 - May 7th 2018</p>
  </div>

  <p class="sport-name">CRICKET</p>
</main>
</body>
</html>
```